Buch-/E-Book-Cover für Sammlung von positiven Erfahrungen
Zielgruppe
die Zielgruppe sind Väter die ihren Söhne eine Sammlung von Empfehlungen für ein positives Leben schenken sollen. Der Titel des Buches heisst 'Zwischen Ebbe und Glut'
Aufgabenstellung
ich möchte mich hier von den Designern überraschen und inspirieren lassen.

```html
<!DOCTYPE html>
<html lang="de">
<head>
<meta charset="utf-8">
<title>Zwischen Ebbe und Glut – Buchumschlag</title>
<link rel="stylesheet" href="https://fonts.googleapis.com/css2?family=Bebas+Neue&family=Roboto:wght@300;400&family=Arimo&display=swap">
<style>
:root{
  --cover-blue:#b8c7d5;
  --ink:#1c1c1c;
  --band-navy:#0a0b28;
  --band-bronze:#9a6a3c;
  --paper-white:#ffffff;
  --photo-lake:#9fb6c6;
  --photo-sky:#d6dde6;
  --photo-wood:#5a534b;
}
*{margin:0;padding:0;box-sizing:border-box}
html,body{width:1200px;height:793px;overflow:hidden;background:var(--cover-blue)}
.cover{position:relative;width:1200px;height:793px;background:var(--cover-blue);overflow:hidden;color:var(--ink)}
.front-photo{position:absolute;left:664px;top:0;width:536px;height:300px;
  background:linear-gradient(180deg,var(--photo-sky) 0%,var(--photo-lake) 45%,var(--photo-lake) 75%,var(--cover-blue) 100%)}
.front-photo .jetty{position:absolute;left:0;top:0;width:370px;height:160px;
  background:linear-gradient(180deg,#7a7269 0%,var(--photo-wood) 100%);opacity:.55}
.back-title{position:absolute;left:28px;top:24px;font:400 56px/1 "Bebas Neue",sans-serif;letter-spacing:.5px}
.back-copy{position:absolute;font:400 10.4px/17.2px "Arimo",sans-serif;color:#111}
.back-copy p+p{margin-top:17px}
.copy-main{left:30px;top:98px;width:458px}
.copy-bio{left:182px;top:426px;width:312px}
.back-rule{position:absolute;left:30px;top:384px;width:474px;height:2px;background:var(--ink)}
.author-photo{position:absolute;left:28px;top:432px;width:124px;height:160px;background:#000}
.code-area{position:absolute;left:304px;top:656px;width:181px;height:95px;background:var(--paper-white)}
.spine-author,.spine-title{position:absolute;writing-mode:vertical-rl;white-space:nowrap}
.spine-author{left:587px;top:18px;font:300 22px/1 "Roboto",sans-serif;letter-spacing:3px}
.spine-title{left:588px;top:296px;font:400 46px/1 "Bebas Neue",sans-serif;letter-spacing:1px}
.front-title{position:absolute;left:748px;top:272px;width:386px;text-align:center;font-weight:400}
.title-small{display:flex;align-items:center;gap:14px;font:400 30px/1 "Bebas Neue",sans-serif;letter-spacing:1px}
.title-small::before,.title-small::after{content:"";flex:1;height:2px;background:var(--ink)}
.title-big{display:block;font:400 150px/.86 "Bebas Neue",sans-serif;letter-spacing:2px;margin:6px 0 6px}
.title-rule{display:block;height:2px;background:var(--ink);margin-top:16px}
.subtitle{position:absolute;left:742px;top:632px;width:398px;text-align:center;font:300 19.5px/30px "Roboto",sans-serif;letter-spacing:.3px}
.bottom-band{position:absolute;left:0;top:718px;width:1200px;height:75px;background:var(--band-navy)}
.bottom-band::before{content:"";position:absolute;left:0;top:0;width:100%;height:8px;
  background:linear-gradient(90deg,#c8b49a 0%,var(--band-bronze) 30%,var(--band-bronze) 70%,#b78a5c 100%)}
.band-author{position:absolute;left:740px;top:743px;width:390px;text-align:center;color:var(--paper-white);font:400 30px/1 "Roboto",sans-serif;letter-spacing:4.5px}
</style>
</head>
<body>
<main class="cover">
  <div class="front-photo" role="img" aria-label="Foto: Kinderfüße baumeln von einem Holzsteg über einem Bergsee"><div class="jetty"></div></div>

  <h2 class="back-title">ZWISCHEN EBBE UND GLUT</h2>
  <div class="back-copy copy-main">
    <p>Lorem Ipsum is simply dummy text of the printing and typesetting industry. Lorem Ipsum has been the industry's standard dummy text ever since the 1500s, when an unknown printer took a galley of type and scrambled it to make a type specimen book. It has survived not only five centuries, but also the leap into electronic typesetting, remaining essentially unchanged. It was popularised in the 1960s with the release of Pressmark sheets containing Lorem Ipsum passages, and more recently with desktop publishing software like Quillset Layout including versions of Lorem Ipsum.</p>
    <p>Lorem Ipsum is simply dummy text of the printing and typesetting industry. Lorem Ipsum has been the industry's standard dummy text ever since the 1500s, when an unknown printer took a galley of type and scrambled it to make a type specimen book. It has survived not only five centuries, but also the leap into electronic typesetting, remaining essentially unchanged. It was popularised in the 1960s with the release of Pressmark sheets containing Lorem Ipsum passages, and more recently with desktop publishing software like Quillset Layout including versions of Lorem Ipsum.</p>
  </div>
  <div class="back-rule"></div>
  <div class="author-photo"></div>
  <div class="back-copy copy-bio">
    <p>Lorem Ipsum is simply dummy text of the printing and typesetting industry. Lorem Ipsum has been the industry's standard dummy text ever since the 1500s, when an unknown printer took a galley of type and scrambled it to make a type specimen book. It has survived not only five centuries, but also the leap into electronic typesetting, remaining essentially unchanged. It was popularised in the 1960s with the release of Pressmark sheets containing Lorem Ipsum passages, and more recently with desktop publishing software like Quillset Layout including versions of Lorem</p>
  </div>

  <div class="spine-author">LORENZ WITTMAR</div>
  <div class="spine-title">ZWISCHEN EBBE UND GLUT</div>

  <h1 class="front-title">
    <span class="title-small">ZWISCHEN</span>
    <span class="title-big">EBBE</span>
    <span class="title-small">UND</span>
    <span class="title-big">GLUT</span>
    <span class="title-rule"></span>
  </h1>
  <p class="subtitle">EINE SAMMLUNG VON EMPFEHLUNGEN<br>FÜR EIN POSITIVES LEBEN</p>

  <div class="bottom-band"></div>
  <div class="code-area"></div>
  <div class="band-author">LORENZ WITTMAR</div>
</main>
</body>
</html>
```